Elegant sophisticated Invitation Design in A5

"Velvet Evening in the Garden"
We are after an invitation A5 portrait size. It is for an outdoor event for a 4 course dinner. It needs to display high class, elegance and sophistication. We like the idea of having stars or reflections on the water (as per attached images we found on google)

Text and logo are attached. The file needs to be supplied to use as psd file and needs to be 300dpi at least as the invitation will be printed.

We would like dark colours, black, and sparkles/stars.

The main focus is elegance!

Logos and text are attached.

Target Market(s)

Upper class, business men and women, Suit and tie event

Industry/Entity Type

Event

Font styles to use
Decorative
Script

Colors
fffefe
000000

Requirements
Must have
• The element of Water and stars or sparkles. It needs to speak elegance throughout. The fonts chosen need to be soft and elegant. The logo attached must be used either with the diamond or the standard version a mono version can also be used. Open for designers ideas.
Should not have
• Bold and bulky fonts it needs to be soft

```html
<!DOCTYPE html>
<html lang="en">
<head>
<meta charset="utf-8">
<title>Velvet Evening in the Garden – VIP Dinner Invitation</title>
<link rel="stylesheet" href="https://fonts.googleapis.com/css2?family=Didact+Gothic&family=Montserrat:wght@600&family=Pinyon+Script&display=swap">
<style>
  :root {
    --night: #000000;
    --white: #fffefe;
    --cream: #f7f1cc;
    --gold: #e6d79a;
    --rule: #bdbdbd;
    --water-deep: #04153a;
    --water-mid: #0a4ea8;
    --water-light: #3d9be8;
  }
  * { margin: 0; padding: 0; box-sizing: border-box; }
  html, body { width: 845px; height: 1200px; overflow: hidden; background: var(--night); }
  .invitation {
    position: relative;
    width: 845px;
    height: 1200px;
    background: var(--night);
    color: var(--white);
    font-family: "Didact Gothic", "Century Gothic", sans-serif;
    text-align: center;
    overflow: hidden;
  }
  .invitation > * { position: absolute; left: 0; right: 0; }

  .host-mark { top: 84px; }
  .host-mark__dot {
    display: block; width: 14px; height: 14px; margin: 0 auto 14px;
    border-radius: 50%; background: var(--white);
  }
  .host-mark__name { font-size: 40px; letter-spacing: 1px; line-height: 1; color: var(--white); }

  .presenter { top: 199px; font-size: 25px; letter-spacing: 0.5px; color: var(--white); }
  .event-title {
    top: 244px; font-family: "Pinyon Script", cursive;
    font-size: 44px; color: var(--gold); line-height: 1.2;
  }
  .tier {
    top: 315px; left: 320px; right: auto; width: 192px;
    border-top: 1px solid var(--rule); border-bottom: 1px solid var(--rule);
    padding: 6px 0 5px; font-size: 29px; letter-spacing: 0.5px; line-height: 1.15;
  }
  .dinner-name { top: 372px; font-size: 58px; color: var(--cream); line-height: 1.1; }
  .date { top: 459px; font-size: 27px; color: var(--cream); }

  .venue { top: 527px; font-family: "Montserrat", sans-serif; font-weight: 600; font-size: 25px; letter-spacing: 0.5px; }
  .address { top: 565px; font-size: 21px; }

  .cause { top: 628px; font-size: 24px; line-height: 32px; color: var(--cream); letter-spacing: 0.4px; }

  .access {
    top: 714px; left: 169px; right: auto; width: 507px;
    font-family: "Montserrat", sans-serif; font-weight: 600; font-size: 23px;
    padding-bottom: 9px; border-bottom: 1px solid #7a7a7a;
  }

  .highlights { top: 772px; left: 228px; right: auto; list-style: none; text-align: left; font-size: 19px; line-height: 25px; }
  .highlights__item { position: relative; padding-left: 34px; }
  .highlights__item::before { content: "★"; position: absolute; left: 2px; top: 0; font-size: 17px; }
  .highlights__item + .highlights__item { margin-top: 28px; }

  .water {
    top: 958px; bottom: 0;
    background:
      radial-gradient(ellipse 22% 60% at 47% 95%, rgba(220,240,255,0.75), rgba(120,190,255,0) 70%),
      linear-gradient(180deg, #000 0%, var(--water-light) 3%, var(--water-mid) 22%, var(--water-deep) 55%, var(--water-mid) 85%, var(--water-light) 100%);
  }
</style>
</head>
<body>
<main class="invitation">
  <header class="host-mark">
    <span class="host-mark__dot"></span>
    <p class="host-mark__name">Wattlebrook Care</p>
  </header>

  <p class="presenter">Wattlebrook Care's inaugural</p>
  <h1 class="event-title">Velvet Evening in the Garden</h1>
  <p class="tier">VIP DINNER</p>
  <h2 class="dinner-name">Le Banquet</h2>
  <p class="date">Saturday 17th July 2017</p>

  <p class="venue">HARBOURSIDE HERITAGE PARK</p>
  <p class="address">Quay Street, South Harbourton</p>

  <p class="cause">Building accessible housing for people<br>with disability in North Queensland</p>

  <p class="access">BY INVITATION</p>

  <ul class="highlights">
    <li class="highlights__item">Four course dinner exclusively crafted<br>by Salt &amp; Ember Kitchen</li>
    <li class="highlights__item">Beautiful wines and fine beers included</li>
    <li class="highlights__item">Live Entertainment</li>
  </ul>

  <div class="water" role="img" aria-label="Photograph of deep blue water at night with sparkling starlight reflections"></div>
</main>
</body>
</html>
```